Pamphlet for IT Services Company (MSP Provider or Managed Services Provider)

We need a pamphlet designed for our Managed Services Company. We are an established company of 17 years that has never advertised. We'd like a pamphlet that we can drop off at potential client sites that describes our services. I like clean and prefer Orange as an accent color. We'd like to touch on the fact that we cater to our clients needs and go above and beyond what the other providers do.

Target Market(s)

Small and Medium Sized Businesses

Industry/Entity Type

It Service

Font styles to use
Other font styles liked:
• Try to match font on logo or website

Requirements
Must have
• Must highlight with the following Services and descriptions with Logo
Managed IT Services
IT Support
VOIP Solutions
WiFI Solutions
Contact information with phone number and website address.
Please view website korvanetpro.com
try to match fons on website above.
Nice to have
• Customer Testimonials. May a couple one line testimonials. Not real sure because this is the first time we've ever designed a brochure.
Should not have
• Not Sure

```html
<!DOCTYPE html>
<html lang="en">
<head>
<meta charset="utf-8">
<title>Korvanet Technologies – Managed IT Services</title>
<link rel="stylesheet" href="https://fonts.googleapis.com/css2?family=Dosis:wght@300;400;500;600;700;800&display=swap">
<style>
  :root {
    --orange: #f5862e;
    --navy: #1e2838;
    --navy-soft: #2c3647;
    --slate: #6a7d93;
    --steel: #36495f;
    --cream: #fdf8f0;
    --white: #ffffff;
    --ink: #1d1d1f;
    --badge-grey: #d9d9d9;
    --badge-dark: #555555;
  }
  * { margin: 0; padding: 0; box-sizing: border-box; }
  html, body { width: 848px; height: 1200px; overflow: hidden; background: var(--white); }
  body { font-family: "Dosis", sans-serif; }
  .flyer { position: relative; width: 848px; height: 1200px; overflow: hidden; background: var(--navy); }

  .masthead { position: absolute; left: 0; top: 0; width: 848px; height: 96px; background: var(--cream); }
  .brand-name {
    position: absolute; right: 32px; top: 26px;
    font-size: 34px; font-weight: 400; color: var(--orange); letter-spacing: 0.2px;
  }

  .hero-art { position: absolute; left: 0; top: 96px; width: 848px; height: 612px; }

  .tagline {
    position: absolute; left: 97px; top: 483px;
    color: var(--white); font-size: 33px; line-height: 43px; font-weight: 300;
  }
  .tagline strong { font-weight: 700; }

  .hero-title {
    position: absolute; right: 56px; top: 543px; text-align: right;
    color: var(--white); font-size: 64px; line-height: 68px; font-weight: 700; letter-spacing: 0.5px;
  }

  .services { position: absolute; left: 42px; top: 739px; width: 765px; height: 254px; display: flex; }
  .service { flex: 1; padding: 20px 14px 0; text-align: center; }
  .service--managed { background: var(--slate); color: var(--white); }
  .service--support { background: var(--cream); color: var(--ink); }
  .service--voip { background: var(--orange); color: var(--ink); }
  .service--wifi { background: var(--steel); color: var(--white); }
  .service-icon { width: 34px; height: 34px; margin: 0 auto; display: block; }
  .service-title { margin-top: 22px; font-size: 17px; font-weight: 600; }
  .service-text { margin-top: 12px; font-size: 8.6px; line-height: 11.5px; font-weight: 600; }
  .service-text p + p { margin-top: 8px; }

  .contact { position: absolute; left: 271px; top: 1021px; display: flex; align-items: center; gap: 12px; }
  .contact-icon { width: 30px; height: 30px; }
  .contact-label { color: var(--orange); font-size: 15px; font-weight: 600; line-height: 16px; }
  .contact-number { color: var(--white); font-size: 27px; font-weight: 700; line-height: 28px; }

  .partners { position: absolute; left: 0; top: 1088px; width: 848px; height: 112px; background: var(--white); }
  .badge { position: absolute; background: var(--badge-grey); }
  .badge--square { left: 56px; top: 14px; width: 72px; height: 73px; background: none; border: 1px solid var(--badge-grey); }
  .badge--square::after { content: ""; position: absolute; left: 18px; top: 18px; width: 34px; height: 34px; background: var(--badge-grey); }
  .badge--one { left: 139px; top: 30px; width: 64px; height: 38px; }
  .badge--two { left: 165px + 0; }
  .badge--wide-top { left: 214px; top: 22px; width: 118px; height: 20px; }
  .badge--wide-bottom { left: 218px; top: 52px; width: 112px; height: 18px; }
  .badge--four { left: 356px; top: 34px; width: 116px; height: 34px; }
  .badge--premier { left: 520px; top: 11px; width: 269px; height: 83px; background: var(--badge-dark); }
</style>
</head>
<body>
<main class="flyer">
  <header class="masthead">
    <div class="brand-name">korvanet technologies</div>
  </header>

  <svg class="hero-art" viewBox="0 96 848 612" width="848" height="612">
    <defs>
      <linearGradient id="deskTone" x1="0" y1="0" x2="1" y2="1">
        <stop offset="0" stop-color="#8a5a36"/>
        <stop offset="0.5" stop-color="#7a4c2c"/>
        <stop offset="1" stop-color="#5e3a22"/>
      </linearGradient>
    </defs>
    <rect x="0" y="96" width="848" height="612" fill="url(#deskTone)" role="img"
          aria-label="Overhead photo of a wooden office desk with a monitor, keyboard, laptop, files, coffee cup and a small plant"/>
    <rect x="0" y="515" width="848" height="193" fill="var(--navy-soft)" opacity="0.92"/>
    <polygon points="0,135 468,708 110,708 0,567" fill="var(--orange)"/>
    <polygon points="0,567 110,708 0,708" fill="var(--navy)"/>
  </svg>

  <h2 class="tagline"><strong>A Simple,</strong><br>Cost Effective<br>Plan for your<br>IT Infrastructure.</h2>
  <h1 class="hero-title">MANAGED<br>IT SERVICES</h1>

  <section class="services">
    <article class="service service--managed">
      <svg class="service-icon" viewBox="0 0 34 34"><path d="M6 4h22v13c0 7-5 11-11 13C11 28 6 24 6 17z" fill="var(--white)"/><path d="M17 8h7v9c0 4-3 7-7 8z" fill="var(--slate)"/></svg>
      <h3 class="service-title">Managed IT Services</h3>
      <div class="service-text">
        <p>Let us take care of your IT</p>
        <p>Our MSP is a Flat Rate service that includes Onsite &amp; Remote Support, Endpoint Protection, Web Filtering, Encrypted Online Backup &amp; Patch Management</p>
      </div>
    </article>
    <article class="service service--support">
      <svg class="service-icon" viewBox="0 0 34 34" fill="none" stroke="var(--ink)" stroke-width="2.6"><circle cx="17" cy="11" r="7"/><path d="M5 31c0-7 5-11 12-11s12 4 12 11z" stroke-linejoin="round"/></svg>
      <h3 class="service-title">IT Support</h3>
      <div class="service-text">
        <p>We have a passion for what we do and it shows! Korvanet provides fast, reliable, expert solutions from experienced staff. You will never feel like just another client to us because our customers are family!</p>
      </div>
    </article>
    <article class="service service--voip">
      <svg class="service-icon" viewBox="0 0 34 34"><path d="M9 6l5 0 1 7-4 2c1 4 3 7 6 9l3-3 6 2v5c-11 1-20-9-19-22z" fill="var(--ink)" transform="rotate(-10 17 17)"/><path d="M21 6a7 7 0 0 1 6 6M22 2a11 11 0 0 1 9 9" fill="none" stroke="var(--ink)" stroke-width="2.4" stroke-linecap="round"/></svg>
      <h3 class="service-title">VOIP Solutions</h3>
      <div class="service-text">
        <p>Phones are more than just an attachment to a desk. Allow us to help you maximize communication with your team and customers by using the latest technology that will likely save you money as well. Korvanet Technologies partners with Vantel to provide phone hardware, systems, and phone service</p>
      </div>
    </article>
    <article class="service service--wifi">
      <svg class="service-icon" viewBox="0 0 34 34" fill="none" stroke="var(--white)" stroke-width="3.4" stroke-linecap="round"><path d="M3 13a20 20 0 0 1 28 0"/><path d="M8 18a13 13 0 0 1 18 0"/><path d="M13 23a6 6 0 0 1 8 0"/><circle cx="17" cy="28" r="1.8" fill="var(--white)" stroke="none"/></svg>
      <h3 class="service-title">WiFi Solutions</h3>
      <div class="service-text">
        <p>WiFi is everywhere! (At least it should be.) Korvanet can extend your WiFi to cover your whole campus</p>
      </div>
    </article>
  </section>

  <div class="contact">
    <svg class="contact-icon" viewBox="0 0 30 30"><circle cx="15" cy="15" r="15" fill="var(--orange)"/><path d="M9 8h4l1 4-2 2c1 2 3 4 5 5l2-2 4 1v4c-8 1-15-6-14-14z" fill="var(--white)"/></svg>
    <div>
      <div class="contact-label">Call Us</div>
      <div class="contact-number">+1 (555) 014-2290</div>
    </div>
  </div>

  <footer class="partners" aria-label="Partner badges">
    <div class="badge badge--square"></div>
    <div class="badge badge--one"></div>
    <div class="badge badge--wide-top"></div>
    <div class="badge badge--wide-bottom"></div>
    <div class="badge badge--four"></div>
    <div class="badge badge--premier"></div>
  </footer>
</main>
</body>
</html>
```